Business Card Design

I am a Special Event Consultant,I arrange and organise Special Events - Product Launches,Sponsorship and Product Displays.

I would like the TRV to be a feature of the design with 'Fine Occasion Services" underneath - keep it very simple but creative using this information. So it is just the letters "TRV" with Event Services underneath.

(Simple Colours - Silver, Black, Grey - no bright colours - We work for Valdoren Kraft,QJX, Tavrelli So it is class and classic.)

Only my Name and mobile on the front.

Industry/Entity Type

Business

Contact Information for Business Card

FRONT
Jo Pettigrew
Tel: 0427 318906

BACK
Email: jo@trvoccasionhire.com.au

1208 Wexley Court,72 Ormond Lane
KELMSTON.Vic.3145.

```html
<!DOCTYPE html>
<html lang="en">
<head>
<meta charset="utf-8">
<title>TRV Fine Occasion Services – Business Card</title>
<link rel="stylesheet" href="https://fonts.googleapis.com/css2?family=Josefin+Sans:wght@300;400&display=swap">
<style>
  :root {
    --bg: #e9e9e9;
    --card-white: #ffffff;
    --card-silver: #b4b4b4;
    --band-grey: #6e6e6e;
    --band-black: #0a0a0a;
    --ink: #1a1a1a;
    --rule: #555555;
    --strip-grey: #b9b9b9;
    --on-dark: #f2f2f2;
  }
  * { box-sizing: border-box; margin: 0; padding: 0; }
  html, body {
    width: 1200px; height: 800px; overflow: hidden;
    background: var(--bg);
    font-family: "Josefin Sans", "Century Gothic", sans-serif;
  }
  .canvas {
    position: relative; width: 1200px; height: 800px;
    display: flex; align-items: center; justify-content: center; gap: 30px;
  }
  .card {
    position: relative; width: 535px; height: 306px;
    border-radius: 8px; overflow: hidden;
    box-shadow: 0 2px 6px rgba(0,0,0,0.15);
  }

  /* Back side */
  .card--back { background: var(--card-silver); }
  .contact-band {
    position: absolute; left: 0; right: 0; top: 112px; height: 128px;
    background: var(--band-grey);
    border-top: 24px solid var(--band-black);
    border-bottom: 24px solid var(--band-black);
    display: flex; align-items: center; justify-content: space-between;
    padding: 0 34px 0 44px;
    color: var(--on-dark);
    font-weight: 300; font-size: 10.5px; letter-spacing: 0.08em;
    text-transform: uppercase; line-height: 1.45;
  }
  .contact-item { display: flex; align-items: center; gap: 12px; }
  .contact-item svg { flex: none; }
  .contact-item address { font-style: normal; }

  /* Front side */
  .card--front { background: var(--card-white); color: var(--ink); }
  .holder-name {
    position: absolute; left: 42px; top: 66px;
    font-weight: 300; font-size: 25px; letter-spacing: 0.06em; text-transform: uppercase;
  }
  .holder-role {
    position: absolute; left: 42px; top: 96px; right: 42px;
    display: flex; align-items: center; gap: 6px;
    font-weight: 300; font-size: 8.5px; letter-spacing: 0.08em; text-transform: uppercase;
  }
  .holder-role .rule { flex: 1; height: 1px; background: var(--rule); margin-top: 8px; }
  .holder-phone {
    position: absolute; right: 58px; top: 198px;
    display: flex; align-items: center; gap: 14px;
    font-weight: 300; font-size: 18px; letter-spacing: 0.08em;
  }
  .holder-phone svg { flex: none; }
  .service-strip {
    position: absolute; left: 0; right: 0; bottom: 0; height: 28px;
    background: var(--strip-grey); color: var(--on-dark);
    display: flex; align-items: center; justify-content: center;
    font-weight: 300; font-size: 8.5px; letter-spacing: 0.14em; text-transform: uppercase;
  }
</style>
</head>
<body>
<main class="canvas">

  <section class="card card--back" aria-label="Card back">
    <div class="contact-band">
      <div class="contact-item">
        <svg width="18" height="18" viewBox="0 0 18 18" aria-hidden="true">
          <circle cx="9" cy="9" r="8.5" fill="#f2f2f2"/>
          <path d="M9 4.2a3 3 0 0 0-3 3c0 2.2 3 5.8 3 5.8s3-3.6 3-5.8a3 3 0 0 0-3-3z" fill="#6e6e6e"/>
          <circle cx="9" cy="7.2" r="1.1" fill="#f2f2f2"/>
        </svg>
        <address>1208 Wexley Court<br>72 Ormond Lane<br>Kelmston.Vic.3145</address>
      </div>
      <div class="contact-item">
        <svg width="18" height="18" viewBox="0 0 18 18" aria-hidden="true">
          <circle cx="9" cy="9" r="8.5" fill="#f2f2f2"/>
          <rect x="4.5" y="6" width="9" height="6.2" fill="#6e6e6e"/>
          <path d="M4.5 6 9 9.6 13.5 6" fill="none" stroke="#f2f2f2" stroke-width="0.8"/>
        </svg>
        <span>jo@trvoccasionhire.com.au</span>
      </div>
    </div>
  </section>

  <section class="card card--front" aria-label="Card front">
    <h1 class="holder-name">Jo Pettigrew</h1>
    <p class="holder-role"><span>Event Consultant</span><span class="rule"></span></p>
    <p class="holder-phone">
      <svg width="18" height="18" viewBox="0 0 18 18" aria-hidden="true">
        <circle cx="9" cy="9" r="8.5" fill="none" stroke="#1a1a1a" stroke-width="1"/>
        <path d="M7 5h1.6l.6 2-1 .8a5 5 0 0 0 2 2l.8-1 2 .6V11a1 1 0 0 1-1 1A6 6 0 0 1 6 6a1 1 0 0 1 1-1z" fill="#1a1a1a"/>
      </svg>
      <span>0427 318906</span>
    </p>
    <div class="service-strip">Fine Occasion Services</div>
  </section>

</main>
</body>
</html>
```